LoanHaven Mortgage Business Cards

We are a relatively new mortgage company, and we need business cards. We'd like a modern design. We want our business cards to grab attention without being too dramatic or presumptuous.
Our name: LoanHaven Mortgage. Our logos in horizontal and vertical executions are attached.
Our contact info:
2871 Maple Terrace Blvd, Suite 415
Las Vegas, NV 89047
702-514-7390
We need the following disclaimer:
©2017 A division of Lending of Horizon Mortgage LLC | Equal Housing Lender | NMLS ID # 5823 | Mortgage Banker License #0637492 | Licensed by the Department of Business Oversight under the California Residential Mortgage Lending Act
We would like an option with and an option without a photo of the employee. For the design let's use this info:
Dana Morrow, MBA
Director
NMLS # 584216
Direct Office: (702) 514-7381
Cell: (702) 926-1587
Fax: (844) 763-2018
dana.morrow@loanhvn.example
Dana's photo is attached.
We'd like a double-sided card. It might be interesting to use our brand red (#f40000) on the back. As a thought starter, see attached for how our customer letters look.
Standard size. See description for brief.

```html
<!DOCTYPE html>
<html lang="en">
<head>
<meta charset="utf-8">
<title>LoanHaven Mortgage – Business Card</title>
<link rel="stylesheet" href="https://fonts.googleapis.com/css2?family=Montserrat:wght@500;600;700&display=swap">
<style>
  :root {
    --brand-red: #ec1c24;
    --brand-red-light: #ef3a47;
    --card-black: #000000;
    --card-charcoal: #2a2a2a;
    --ink-white: #ffffff;
    --page-bg: #ece9e4;
  }
  * { box-sizing: border-box; margin: 0; padding: 0; }
  html, body { width: 1200px; height: 1000px; overflow: hidden; }
  body {
    background: var(--page-bg);
    font-family: "Montserrat", "Century Gothic", sans-serif;
    position: relative;
  }
  .card {
    position: absolute;
    width: 700px;
    height: 400px;
    border-radius: 4px;
    box-shadow: 0 10px 30px rgba(0,0,0,.18);
    overflow: hidden;
  }
  /* Front */
  .card--front {
    left: 130px; top: 70px;
    background: linear-gradient(100deg, var(--brand-red) 0%, var(--brand-red) 45%, var(--brand-red-light) 100%);
    display: flex; align-items: center; justify-content: center; gap: 22px;
  }
  .front-mark {
    width: 70px; height: 70px; border-radius: 50%;
    background: var(--ink-white);
  }
  .front-name {
    color: var(--ink-white);
    font-weight: 700;
    font-size: 52px;
    letter-spacing: -0.5px;
  }
  /* Back */
  .card--back {
    left: 370px; top: 520px;
    background: linear-gradient(90deg, var(--card-black) 0%, var(--card-black) 45%, var(--card-charcoal) 100%);
    color: var(--ink-white);
  }
  .accent-bar {
    position: absolute; height: 10px; background: var(--ink-white);
  }
  .accent-bar--top { top: 0; left: 350px; right: 0; }
  .accent-bar--bottom { bottom: 0; left: 440px; right: 0; }
  .brand-lockup {
    position: absolute; left: 44px; top: 92px;
    display: flex; align-items: center; gap: 12px;
  }
  .brand-lockup__mark {
    width: 34px; height: 34px; border-radius: 50%; background: var(--ink-white);
  }
  .brand-lockup__name {
    font-weight: 700; font-size: 28px; color: var(--ink-white); letter-spacing: -0.3px;
  }
  .contact {
    position: absolute; left: 420px; top: 48px;
  }
  .contact__name { font-weight: 700; font-size: 17px; line-height: 1.2; }
  .contact__credential { color: var(--brand-red); }
  .contact__title { font-weight: 700; font-size: 17px; margin-bottom: 20px; }
  .contact__list { list-style: none; margin-left: 38px; }
  .contact__item {
    display: flex; align-items: center; gap: 10px;
    font-weight: 600; font-size: 16px; margin-bottom: 8px; letter-spacing: .4px;
  }
  .contact__item svg { width: 18px; height: 18px; fill: var(--brand-red); flex: none; }
  .contact__email {
    position: absolute; right: 40px; top: 260px;
    font-weight: 600; font-size: 17px; letter-spacing: .3px;
  }
</style>
</head>
<body>
  <section class="card card--front" aria-label="Card front">
    <span class="front-mark"></span>
    <span class="front-name">LoanHaven</span>
  </section>

  <section class="card card--back" aria-label="Card back">
    <span class="accent-bar accent-bar--top"></span>
    <span class="accent-bar accent-bar--bottom"></span>

    <div class="brand-lockup">
      <span class="brand-lockup__mark"></span>
      <span class="brand-lockup__name">LoanHaven Mortgage</span>
    </div>

    <div class="contact">
      <p class="contact__name">Dana Morrow, <span class="contact__credential">MBA</span></p>
      <p class="contact__title">Director</p>
      <ul class="contact__list">
        <li class="contact__item">
          <svg viewBox="0 0 24 24" aria-hidden="true"><path d="M7 2h10a2 2 0 0 1 2 2v16a2 2 0 0 1-2 2H7a2 2 0 0 1-2-2V4a2 2 0 0 1 2-2zm0 3v13h10V5H7zm5 14.2a1 1 0 1 0 0 .1z"/></svg>
          (702) 514-7381
        </li>
        <li class="contact__item">
          <svg viewBox="0 0 24 24" aria-hidden="true"><path d="M2 9c3-4 17-4 20 0l-1 3h-4l-1-2c-2-.6-6-.6-8 0l-1 2H3L2 9zm4 4h12l2 7H4l2-7zm6 1.5a2.5 2.5 0 1 0 0 5 2.5 2.5 0 0 0 0-5z"/></svg>
          (702) 926-1587
        </li>
        <li class="contact__item">
          <svg viewBox="0 0 24 24" aria-hidden="true"><path d="M6 2h9l3 3v4H6V2zM3 10h18a1 1 0 0 1 1 1v7h-4v4H6v-4H2v-7a1 1 0 0 1 1-1zm5 6v4h8v-4H8z"/></svg>
          (844) 763-2018
        </li>
      </ul>
    </div>

    <p class="contact__email">dana.morrow@loanhvn.example</p>
  </section>
</body>
</html>
```